I am a company selling interior designing materials

HI, I am selling interior design materials and require a namecard which is more outstanding while following a certain details placement as attached.

My clients are mainly interior designers so it has to attract their attention rather than feeling that its "just another namecard". I am selling wallcoverings, fabrics, acoustics and carpets.

Target Market(s)

interior designers designing hotels, commerical offices.

Contact Information for Business Card

As per attached.
Please change address to 47 Jalan 16 Tampines #05-02 Velmora Building Singapore 527314

Font styles to use
Other font styles liked:
• calibri

Requirements
Must have
• (1) company logo on top in the middle. Placement of contac details to be the same
• (2) company color is blue/green cymk 75/8/42/0
• (3) "KTV" logo to be prominent
• (4) You may change the logo but there should be a "swirl" surrounding the word KTV like current logo. The swirl pattern does not need to follow current logo and you may propose.
Should not have
• (1) there should not be any designs above "KTV" logo
• (2) no sharp triangles or angles

```html
<!DOCTYPE html>
<html lang="en">
<head>
<meta charset="utf-8">
<title>KTV Business Card</title>
<link rel="stylesheet" href="https://fonts.googleapis.com/css2?family=Carlito:wght@400;700&family=Open+Sans:wght@600;700;800&display=swap">
<style>
  :root {
    --backdrop: #c8e6dc;
    --card-white: #ffffff;
    --brand-red: #ec1c24;
    --band-grey: #6d6d6d;
    --ink-dark: #4a4a4a;
    --ink-text: #555555;
    --brand-teal: #1fa89a;
    --divider: #8a8a8a;
  }
  * { margin: 0; padding: 0; box-sizing: border-box; }
  html, body {
    width: 1200px; height: 856px; overflow: hidden;
    background: var(--backdrop);
  }
  .canvas {
    width: 1200px; height: 856px;
    display: flex; align-items: center; justify-content: center; gap: 40px;
  }
  .card {
    width: 540px; height: 324px; border-radius: 30px;
    position: relative; overflow: hidden;
    box-shadow: 0 10px 26px rgba(0,0,0,0.12);
  }

  /* Front */
  .card--front { background: var(--card-white); }
  .company-band {
    height: 52px; background: var(--band-grey);
    border-bottom: 2px solid var(--brand-red);
    display: flex; align-items: center; justify-content: center;
    font-family: "Open Sans", sans-serif; font-weight: 700;
    color: #ffffff; font-size: 15.5px; letter-spacing: 1.6px;
  }
  .front-body { position: absolute; top: 54px; left: 0; right: 0; bottom: 0; }
  .brand-mark {
    position: absolute; left: 44px; top: 92px;
    display: flex; align-items: center; gap: 12px;
  }
  .brand-mark__dot {
    width: 26px; height: 26px; border-radius: 50%; background: var(--brand-teal);
  }
  .brand-mark__name {
    font-family: "Open Sans", sans-serif; font-weight: 800;
    font-size: 62px; color: var(--ink-dark); letter-spacing: 1px; line-height: 1;
  }
  .divider {
    position: absolute; left: 238px; top: 36px; height: 172px;
    border-left: 1.5px solid var(--divider);
  }
  .contact { position: absolute; left: 258px; top: 34px; right: 20px; }
  .contact__name {
    font-family: "Open Sans", sans-serif; font-weight: 800;
    font-size: 26px; color: var(--brand-red); letter-spacing: 1px; line-height: 1.1;
    margin-bottom: 12px;
  }
  .contact__line {
    display: flex; align-items: center; gap: 8px;
    font-family: "Carlito", sans-serif; font-size: 17px; color: var(--ink-text);
    line-height: 1.3;
  }
  .contact__line svg { width: 12px; height: 12px; flex: none; }
  .contact__address {
    margin-top: 12px; font-family: "Carlito", sans-serif; font-size: 17px;
    color: var(--ink-text); line-height: 1.25;
  }

  /* Back */
  .card--back {
    background: var(--brand-red); color: #ffffff;
    display: flex; flex-direction: column; align-items: center;
    font-family: "Open Sans", sans-serif;
  }
  .back-mark {
    margin-top: 62px; display: flex; align-items: center; gap: 12px;
  }
  .back-mark__dot { width: 24px; height: 24px; border-radius: 50%; background: #ffffff; }
  .back-mark__name { font-weight: 800; font-size: 58px; line-height: 1; letter-spacing: 1px; }
  .back-company { margin-top: 18px; font-weight: 700; font-size: 16px; letter-spacing: 0.4px; }
  .back-services {
    position: absolute; bottom: 40px; left: 0; right: 0; text-align: center;
    font-weight: 600; font-size: 15px; letter-spacing: 1.6px;
  }
</style>
</head>
<body>
<main class="canvas">
  <section class="card card--front" aria-label="Business card front">
    <header class="company-band">KESTAVEL INTERIOR FURNISHINGS PTE LTD</header>
    <div class="front-body">
      <div class="brand-mark">
        <span class="brand-mark__dot"></span>
        <span class="brand-mark__name">KTV</span>
      </div>
      <div class="divider"></div>
      <div class="contact">
        <h1 class="contact__name">DELIA MARSH</h1>
        <p class="contact__line">
          <svg viewBox="0 0 12 12" aria-hidden="true"><path d="M3 1.2 L4.6 3.4 L3.6 4.6 Q4.8 7.2 7.4 8.4 L8.6 7.4 L10.8 9 L9.8 10.8 Q5.6 10.6 2.6 7.4 Q1 5 1.2 2.2 Z" fill="#ec1c24"/></svg>
          (65) 6217 4480
        </p>
        <p class="contact__line">
          <svg viewBox="0 0 12 12" aria-hidden="true"><rect x="3" y="1" width="6" height="10" rx="1.2" fill="none" stroke="#ec1c24" stroke-width="1.3"/><circle cx="6" cy="9.2" r="0.7" fill="#ec1c24"/></svg>
          (65) 9826 3315
        </p>
        <p class="contact__line">
          <svg viewBox="0 0 12 12" aria-hidden="true"><rect x="1" y="2.5" width="10" height="7" rx="1" fill="none" stroke="#ec1c24" stroke-width="1.2"/><path d="M1.4 3 L6 6.6 L10.6 3" fill="none" stroke="#ec1c24" stroke-width="1.2"/></svg>
          delia@ktvfurnishings.com
        </p>
        <p class="contact__address">47 Jalan 16 Tampines #05-02<br>Velmora Building Singapore 527314</p>
      </div>
    </div>
  </section>

  <section class="card card--back" aria-label="Business card back">
    <div class="back-mark">
      <span class="back-mark__dot"></span>
      <span class="back-mark__name">KTV</span>
    </div>
    <p class="back-company">KesTaVel Interior Furnishings Pte Ltd</p>
    <p class="back-services">WALLCOVERINGS - ACOUSTIC - FABRICS - CARPET</p>
  </section>
</main>
</body>
</html>
```